Bref créative
Stationary Project
BRQ - Bright Rivers Quality
Simple
Dale Morrow
Toms River, NJ
dmorrow@br-quality.example
brightriversquality.example
Industry Type is for Photography. For some reason it does not show when I confirm brief. Add "Bringing Nature Indoors" to project. This font style can be different than the BRQ Logo Font. (possibly script, but must be crisp and clear). Can use color but must not distract from Falcon Image. Also at this point in time, name, email, etc should be in the same font as the Logo but may possibly be changed once designs are submitted and reviewed by my staff.

```html
<!DOCTYPE html>
<html lang="en">
<head>
<meta charset="utf-8">
<title>BRQ - Bright Rivers Quality — Stationery Set</title>
<link href="https://fonts.googleapis.com/css2?family=Cinzel:wght@400;600&family=Cormorant+Garamond:wght@400;600&family=Great+Vibes&family=Open+Sans:wght@400&display=swap" rel="stylesheet">
<style>
:root{
  --backdrop:#4a2c1c;
  --paper:#ffffff;
  --ink:#2b2b2b;
  --ink-soft:#6d6d6d;
  --rule:#9a9a9a;
  --gold:#c9a43a;
  --gold-light:#e9d38a;
  --gold-deep:#a8832a;
  --gray-band:#d9d9d9;
  --mark-tone:#ececec;
  --label:#f3ece4;
}
*{box-sizing:border-box;margin:0;padding:0}
html,body{width:1200px;height:559px;overflow:hidden}
body{background:var(--backdrop);font-family:"Cormorant Garamond",Georgia,serif;color:var(--ink);position:relative}

.piece-label{position:absolute;font-family:"Open Sans",Arial,sans-serif;font-size:8px;color:var(--label);text-align:center}
.sheet{position:absolute;background:var(--paper);overflow:hidden;box-shadow:0 2px 6px rgba(0,0,0,.45)}

/* brand lockup */
.brand{position:absolute;display:flex;flex-direction:column;align-items:flex-start}
.brand-top{display:flex;align-items:center;gap:4px}
.brand-dot{width:9px;height:9px;border-radius:50%;background:var(--ink)}
.brand-mark{font-family:"Cinzel",Georgia,serif;font-weight:600;color:var(--ink);letter-spacing:1px;line-height:1}
.brand-name{font-family:"Cinzel",Georgia,serif;font-weight:600;color:var(--ink);letter-spacing:.6px;line-height:1.2;border-bottom:1px solid var(--ink);padding-bottom:1px}
.brand-tag{font-family:"Cinzel",Georgia,serif;color:var(--ink-soft);letter-spacing:.6px}

.bird-area{position:absolute;background:radial-gradient(ellipse at 50% 45%,var(--mark-tone) 0%,#f4f4f4 55%,rgba(255,255,255,0) 75%)}

.swoosh{position:absolute;left:0;bottom:0;width:100%}

.contact{position:absolute;text-align:left;font-family:"Cinzel",Georgia,serif;color:var(--ink);line-height:1.35}
.contact .person{font-weight:600;letter-spacing:.5px}

/* fax */
.fax-title{position:absolute;right:14px;top:42px;font-family:"Cinzel",Georgia,serif;font-weight:600;font-size:9px;letter-spacing:1px}
.fax-table{position:absolute;left:14px;top:50px;width:323px;border-collapse:collapse;font-family:"Cinzel",Georgia,serif;font-size:6.5px}
.fax-table td{border:1px solid var(--rule);height:16px;padding:0 4px}
.fax-table td.field{width:42px}
.fax-checks{position:absolute;left:14px;top:124px;display:flex;gap:14px;font-family:"Cinzel",Georgia,serif;font-size:6px}
.fax-checks span{display:flex;align-items:center;gap:3px}
.fax-checks i{display:inline-block;width:6px;height:6px;border:1px solid var(--ink)}

.card-back{background:linear-gradient(135deg,var(--gold-light),var(--gold) 50%,var(--gold-deep))}
.card-name{position:absolute;left:0;right:0;top:46px;text-align:center;font-family:"Great Vibes",cursive;font-size:15px;color:var(--ink)}
.card-role{position:absolute;left:0;right:0;top:68px;text-align:center;font-family:"Cinzel",Georgia,serif;font-size:5px;letter-spacing:.8px;color:var(--ink)}
</style>
</head>
<body>

<!-- Fax cover -->
<div class="piece-label" style="left:29px;top:10px;width:351px">Fax Cover</div>
<section class="sheet fax-cover" style="left:29px;top:29px;width:351px;height:504px">
  <div class="brand" style="left:14px;top:12px">
    <div class="brand-top"><span class="brand-mark" style="font-size:20px">BRQ</span><span class="brand-dot"></span></div>
    <span class="brand-name" style="font-size:6px">Bright Rivers Quality</span>
    <span class="brand-tag" style="font-size:4px">Bringing Nature Indoors</span>
  </div>
  <div class="fax-title">FAX</div>
  <table class="fax-table">
    <tr><td class="field">To:</td><td></td><td class="field">Name:</td><td></td></tr>
    <tr><td class="field">Fax:</td><td></td><td class="field">Pages:</td><td></td></tr>
    <tr><td class="field">Phone:</td><td></td><td class="field">Date:</td><td></td></tr>
    <tr><td class="field">Re:</td><td></td><td class="field">CC:</td><td></td></tr>
  </table>
  <div class="fax-checks">
    <span><i></i>Urgent</span><span><i></i>For Review</span><span><i></i>Please Comment</span><span><i></i>Please Reply</span><span><i></i>Please Recycle</span>
  </div>
  <div class="bird-area" role="img" aria-label="Faint falcon illustration watermark" style="left:10px;top:150px;width:230px;height:270px"></div>
  <div class="contact" style="left:240px;top:410px;font-size:5px">
    <div class="person" style="font-size:6px">Dale Morrow</div>
    <div>120 Harbor Lane</div>
    <div>Toms River, NJ 08753</div>
    <div>(732) 555-0148</div>
    <div>dmorrow@br-quality.example</div>
    <div>brightriversquality.example</div>
  </div>
  <svg class="swoosh" viewBox="0 0 351 60" height="60" preserveAspectRatio="none" aria-hidden="true">
    <path d="M0 30 Q120 58 351 20 L351 60 L0 60Z" fill="var(--gray-band)"/>
    <path d="M0 40 Q140 62 351 28" fill="none" stroke="var(--gold)" stroke-width="3"/>
    <path d="M0 48 Q150 66 351 40 L351 60 L0 60Z" fill="#ffffff"/>
  </svg>
</section>

<!-- Letterhead -->
<div class="piece-label" style="left:408px;top:10px;width:351px">Letterhead</div>
<section class="sheet letterhead" style="left:408px;top:29px;width:351px;height:504px">
  <div class="brand" style="left:14px;top:12px">
    <div class="brand-top"><span class="brand-mark" style="font-size:20px">BRQ</span><span class="brand-dot"></span></div>
    <span class="brand-name" style="font-size:6px">Bright Rivers Quality</span>
    <span class="brand-tag" style="font-size:4px">Bringing Nature Indoors</span>
  </div>
  <div class="bird-area" role="img" aria-label="Faint falcon illustration watermark" style="left:30px;top:80px;width:260px;height:330px"></div>
  <div class="contact" style="left:240px;top:410px;font-size:5px">
    <div class="person" style="font-size:6px">Dale Morrow</div>
    <div>120 Harbor Lane</div>
    <div>Toms River, NJ 08753</div>
    <div>(732) 555-0148</div>
    <div>dmorrow@br-quality.example</div>
    <div>brightriversquality.example</div>
  </div>
  <svg class="swoosh" viewBox="0 0 351 60" height="60" preserveAspectRatio="none" aria-hidden="true">
    <path d="M0 30 Q120 58 351 20 L351 60 L0 60Z" fill="var(--gray-band)"/>
    <path d="M0 40 Q140 62 351 28" fill="none" stroke="var(--gold)" stroke-width="3"/>
    <path d="M0 48 Q150 66 351 40 L351 60 L0 60Z" fill="#ffffff"/>
  </svg>
</section>

<!-- Business card front -->
<div class="piece-label" style="left:782px;top:10px;width:154px">Business Card (Front)</div>
<section class="sheet card-front" style="left:782px;top:29px;width:154px;height:120px">
  <div class="brand" style="left:8px;top:6px">
    <div class="brand-top"><span class="brand-mark" style="font-size:13px">BRQ</span><span class="brand-dot" style="width:6px;height:6px"></span></div>
    <span class="brand-name" style="font-size:4px">Bright Rivers Quality</span>
  </div>
  <div class="contact" style="left:92px;top:66px;font-size:3.6px">
    <div class="person" style="font-size:4.4px">Dale Morrow</div>
    <div>120 Harbor Lane</div>
    <div>Toms River, NJ 08753</div>
    <div>(732) 555-0148</div>
    <div>dmorrow@br-quality.example</div>
  </div>
  <svg class="swoosh" viewBox="0 0 154 22" height="22" preserveAspectRatio="none" aria-hidden="true">
    <path d="M0 10 Q60 24 154 6 L154 22 L0 22Z" fill="var(--gray-band)"/>
    <path d="M0 14 Q64 26 154 10" fill="none" stroke="var(--gold)" stroke-width="1.5"/>
    <path d="M0 18 Q70 28 154 16 L154 22 L0 22Z" fill="#ffffff"/>
  </svg>
</section>

<!-- Business card back -->
<div class="piece-label" style="left:950px;top:10px;width:164px">Business Card (Back)</div>
<section class="sheet card-back" style="left:950px;top:29px;width:164px;height:120px">
  <div class="card-name">Dale Morrow</div>
  <div class="card-role">Photographer</div>
</section>

<!-- Envelope front -->
<div class="piece-label" style="left:782px;top:168px;width:394px">Envelope (Front)</div>
<section class="sheet envelope-front" style="left:782px;top:182px;width:394px;height:173px">
  <div class="brand" style="left:14px;top:12px">
    <div class="brand-top"><span class="brand-mark" style="font-size:18px">BRQ</span><span class="brand-dot" style="width:8px;height:8px"></span></div>
    <span class="brand-name" style="font-size:5.5px">Bright Rivers Quality</span>
  </div>
  <div class="contact" style="left:14px;top:62px;font-size:4px">
    <div>120 Harbor Lane</div>
    <div>Toms River, NJ 08753</div>
  </div>
  <svg class="swoosh" viewBox="0 0 394 30" height="30" preserveAspectRatio="none" aria-hidden="true">
    <path d="M0 14 Q150 34 394 8 L394 30 L0 30Z" fill="var(--gray-band)"/>
    <path d="M0 19 Q160 36 394 13" fill="none" stroke="var(--gold)" stroke-width="2"/>
    <path d="M0 24 Q170 38 394 20 L394 30 L0 30Z" fill="#ffffff"/>
  </svg>
</section>

<!-- Envelope back -->
<div class="piece-label" style="left:782px;top:374px;width:394px">Envelope (Back)</div>
<section class="sheet envelope-back" style="left:782px;top:389px;width:394px;height:144px">
  <svg style="position:absolute;inset:0" width="394" height="144" aria-hidden="true">
    <path d="M0 0 L197 72 L394 0" fill="#fafafa" stroke="#bdbdbd" stroke-width="1"/>
    <path d="M0 144 L160 70 M394 144 L234 70" fill="none" stroke="#d6d6d6" stroke-width="1"/>
  </svg>
  <div class="brand" style="left:178px;top:36px;align-items:center">
    <div class="brand-top"><span class="brand-mark" style="font-size:12px">BRQ</span><span class="brand-dot" style="width:5px;height:5px"></span></div>
    <span class="brand-name" style="font-size:3.6px">Bright Rivers Quality</span>
  </div>
</section>

</body>
</html>
```